Book a car wash

The app will have a logo, contact details and address
It will then lead you to booking a service from list
The customer will have a date, day and time

Booking - There are two types of times arrival is the main - day, date, time, service, payment. Each car takes and average of 1.5 hours

Pay by qlink or fundly or merchant

List of services
Bronze $25
Silver $40
Gold $55
Leather Plus $90
Diamond $100
Ruby $100
Standard Vehicle $0
Larger Vehicle & 4wd $10

Target Market(s)

Professionals with time issues
Parents with time management concerns

Industry/Entity Type

It Service

Requirements
Must have
• Logo
Menu list
Payment system
Address and contact details
Basement CarPark - Wexley Court Shopping Centre
Tarvin rd, Claremont
0493520741
Nice to have
• Big fonts and step by step process
Should not have
• No cars or washing items i.e. sponges

```html
<!DOCTYPE html>
<html lang="en">
<head>
<meta charset="utf-8">
<title>Park &amp; Gleam Wexley Court – Booking App Home</title>
<link rel="stylesheet" href="https://fonts.googleapis.com/css2?family=Cinzel:wght@400;700&family=Source+Sans+3:wght@400;600&display=swap">
<style>
  :root {
    --stage: #2a2a2a;
    --status-bg: #000000;
    --status-text: #ffffff;
    --screen-yellow: #ffd92c;
    --screen-yellow-light: #ffe24f;
    --brand-rust: #96300f;
    --brand-dark: #2f2f33;
    --button-rust: #8a2c04;
    --button-edge: #6d2203;
    --button-text: #ffffff;
    --tab-top: #3a3a3c;
    --tab-bottom: #1f1f21;
    --tab-divider: #141415;
    --tab-label: #e6e6e6;
    --tab-icon: #8c8c90;
    --tab-active-glow: #2fb6ff;
  }
  * { box-sizing: border-box; margin: 0; padding: 0; }
  html, body {
    width: 910px; height: 1200px; overflow: hidden;
    background: var(--stage);
  }
  .app-screen {
    position: absolute; left: 135px; top: 32px;
    width: 640px; height: 1136px;
    display: flex; flex-direction: column;
    overflow: hidden;
  }
  .status-bar {
    height: 40px; background: var(--status-bg); color: var(--status-text);
    font-family: "Source Sans 3", sans-serif; font-weight: 600; font-size: 24px;
    display: flex; align-items: center; justify-content: space-between;
    padding: 0 14px;
  }
  .status-bar .carrier { display: flex; align-items: center; gap: 6px; }
  .status-bar .indicators { display: flex; align-items: center; gap: 10px; }
  .home-panel {
    flex: 1; position: relative;
    background: linear-gradient(115deg, var(--screen-yellow) 0%, var(--screen-yellow) 55%, var(--screen-yellow-light) 70%, var(--screen-yellow) 85%);
    display: flex; flex-direction: column; align-items: center;
  }
  .brand-mark {
    margin-top: 150px;
    display: flex; align-items: center; gap: 16px;
    font-family: "Cinzel", serif; font-weight: 700; font-size: 50px;
    color: var(--brand-rust);
  }
  .brand-mark .dot {
    width: 40px; height: 40px; border-radius: 50%;
    background: var(--brand-rust);
  }
  .venue-title {
    margin-top: 230px;
    text-align: center; color: var(--brand-rust);
    font-family: "Cinzel", serif; font-weight: 400; line-height: 1;
  }
  .venue-title .name { display: block; font-size: 54px; }
  .venue-title .place { display: block; font-size: 40px; margin-top: 12px; }
  .venue-title .tagline {
    display: block; font-size: 24px; margin-top: 14px;
    letter-spacing: 10px; color: var(--brand-dark);
  }
  .booking-button {
    position: absolute; left: 122px; top: 862px;
    width: 394px; height: 70px;
    background: var(--button-rust); border: 2px solid var(--button-edge);
    border-radius: 4px; color: var(--button-text);
    font-family: "Source Sans 3", sans-serif; font-size: 34px;
    display: flex; align-items: center; justify-content: center;
  }
  .tab-bar {
    height: 100px; display: flex;
    background: linear-gradient(var(--tab-top), var(--tab-bottom));
    border-top: 2px solid #4a4a4d;
  }
  .tab {
    flex: 1; position: relative;
    display: flex; flex-direction: column; align-items: center; justify-content: flex-end;
    padding-bottom: 12px; gap: 8px;
    border-right: 2px solid var(--tab-divider);
    color: var(--tab-label);
    font-family: "Source Sans 3", sans-serif; font-size: 18px;
  }
  .tab:last-child { border-right: none; }
  .tab svg { width: 44px; height: 40px; fill: var(--tab-icon); }
  .tab.is-active { background: linear-gradient(#2c2c2e, #19191a); }
  .tab.is-active::before {
    content: ""; position: absolute; top: 4px; left: 38px; right: 38px; height: 8px;
    border-radius: 4px; background: var(--tab-active-glow);
    box-shadow: 0 0 10px var(--tab-active-glow);
  }
</style>
</head>
<body>
  <main class="app-screen">
    <header class="status-bar">
      <span class="carrier">
        <svg width="30" height="18" viewBox="0 0 30 18" aria-hidden="true"><g fill="#fff"><rect x="0" y="12" width="4" height="6"/><rect x="6" y="9" width="4" height="9"/><rect x="12" y="6" width="4" height="12"/><rect x="18" y="3" width="4" height="15"/><rect x="24" y="0" width="4" height="18"/></g></svg>
        Volt
      </span>
      <span class="clock">4:20 PM</span>
      <span class="indicators">
        <svg width="20" height="20" viewBox="0 0 20 20" aria-hidden="true"><circle cx="10" cy="10" r="9" fill="#fff"/><path d="M10 4v6h4" stroke="#000" stroke-width="2" fill="none"/></svg>
        <svg width="20" height="20" viewBox="0 0 20 20" aria-hidden="true"><path d="M19 1 1 9l8 2 2 8z" fill="#fff"/></svg>
        <svg width="22" height="22" viewBox="0 0 22 22" aria-hidden="true"><circle cx="11" cy="11" r="9" stroke="#fff" stroke-width="2" fill="none"/><rect x="7" y="10" width="8" height="6" fill="#fff"/><path d="M8.5 10V8a2.5 2.5 0 0 1 5 0v2" stroke="#fff" stroke-width="1.6" fill="none"/></svg>
        <svg width="44" height="20" viewBox="0 0 44 20" aria-hidden="true"><rect x="1" y="2" width="38" height="16" rx="3" stroke="#fff" stroke-width="2" fill="none"/><rect x="4" y="5" width="32" height="10" fill="#fff"/><rect x="40" y="7" width="3" height="6" fill="#fff"/></svg>
      </span>
    </header>

    <section class="home-panel">
      <div class="brand-mark"><span class="dot"></span>Park &amp; Gleam</div>

      <h1 class="venue-title">
        <span class="name">PARK &amp; GLEAM</span>
        <span class="place">WEXLEY COURT</span>
        <span class="tagline">CAR WASH</span>
      </h1>

      <a class="booking-button">Make a Booking</a>
    </section>

    <nav class="tab-bar">
      <div class="tab">
        <svg viewBox="0 0 44 40" aria-hidden="true"><path d="M22 4 4 20h5v16h10V26h6v10h10V20h5z"/></svg>
        Home
      </div>
      <div class="tab">
        <svg viewBox="0 0 44 40" aria-hidden="true"><rect x="6" y="6" width="6" height="6"/><rect x="16" y="7" width="22" height="4"/><rect x="6" y="17" width="6" height="6"/><rect x="16" y="18" width="22" height="4"/><rect x="6" y="28" width="6" height="6"/><rect x="16" y="29" width="22" height="4"/></svg>
        Services
      </div>
      <div class="tab is-active">
        <svg viewBox="0 0 44 40" aria-hidden="true"><rect x="8" y="8" width="28" height="4"/><rect x="8" y="16" width="28" height="4"/><rect x="8" y="24" width="28" height="4"/><rect x="8" y="32" width="28" height="4"/></svg>
        Booking
      </div>
      <div class="tab">
        <svg viewBox="0 0 44 40" aria-hidden="true"><circle cx="22" cy="12" r="8"/><path d="M8 38c0-10 6-15 14-15s14 5 14 15z"/></svg>
        info
      </div>
      <div class="tab">
        <svg viewBox="0 0 44 40" aria-hidden="true"><path d="M32 4l6 6-20 20-8 2 2-8z"/></svg>
        Contact
      </div>
    </nav>
  </main>
</body>
</html>
```